Valdet Company needs a Business Card Design

We just opened our business recently and we need a business card design. Our basic product are clothes and accessories. We would like to see designs that use bright colors like pink, light blue and purple. In addition to that kindly include also our address in the business card which our main office is located in Los Angeles, California.
The final design should communicate that we have affordable price yet high quality brand.

Target Market(s)

young and middle age women

Industry/Entity Type

Business

Contact Information for Business Card

Valdet Apparel and Accessories 3847 North Pelham St. Los Angeles California
Tel: 424-639-8852

Logo Text

Valdet's Apparel and Accessories

Font styles to use
Serif

Requirements
Must have
• there should be a graphic of a sexy lady wearing an elegant dress at the upper left corner of the business card.

```html
<!DOCTYPE html>
<html lang="en">
<head>
<meta charset="UTF-8">
<title>Valdet Apparel and Accessories – Business Card</title>
<link href="https://fonts.googleapis.com/css2?family=Lora:wght@400;700&display=swap" rel="stylesheet">
<style>
  :root {
    --page-bg: #ecebe8;
    --plaid-light: #f29cc4;
    --plaid-mid: #e35a9a;
    --plaid-deep: #c83a7e;
    --dress-dark: #2a1a24;
    --dress-light: #fbe3ee;
    --cream-light: #fbf3d2;
    --cream-deep: #f1dd9c;
    --ring-pink: #e9587a;
    --ring-dots: #fbd6de;
    --medallion: #2d1a29;
    --text-light: #ffffff;
    --icon-pink: #f0607e;
  }
  * { margin: 0; padding: 0; box-sizing: border-box; }
  html, body {
    width: 1200px;
    height: 841px;
    overflow: hidden;
    background: var(--page-bg);
    font-family: "Lora", Georgia, serif;
  }
  .canvas {
    width: 1200px;
    height: 841px;
    display: flex;
    align-items: center;
    justify-content: center;
  }
  .business-card {
    position: relative;
    width: 1050px;
    height: 600px;
    display: flex;
    overflow: hidden;
    box-shadow: 0 10px 30px rgba(0,0,0,0.18);
  }
  .artwork-panel {
    position: relative;
    width: 42%;
    height: 100%;
    background: linear-gradient(135deg, var(--plaid-light) 0%, var(--plaid-mid) 55%, var(--plaid-deep) 100%);
  }
  .dress-illustration {
    position: absolute;
    left: 26%;
    top: 8%;
    width: 50%;
    height: 84%;
    border-radius: 40% 40% 18% 18% / 22% 22% 10% 10%;
    background: linear-gradient(180deg, var(--dress-dark) 0%, var(--dress-dark) 30%, var(--dress-light) 55%, var(--dress-light) 80%, var(--dress-dark) 100%);
    opacity: 0.85;
  }
  .info-panel {
    flex: 1;
    height: 100%;
    display: flex;
    align-items: center;
    justify-content: center;
    background: radial-gradient(circle at 40% 35%, var(--cream-light) 0%, var(--cream-deep) 100%);
  }
  .medallion {
    position: relative;
    width: 480px;
    height: 480px;
    border-radius: 50%;
    background: var(--ring-pink);
    display: flex;
    align-items: center;
    justify-content: center;
  }
  .medallion-dots {
    position: absolute;
    inset: 14px;
    border-radius: 50%;
    border: 4px dotted var(--ring-dots);
  }
  .medallion-core {
    width: 420px;
    height: 420px;
    border-radius: 50%;
    background: var(--medallion);
    color: var(--text-light);
    display: flex;
    flex-direction: column;
    align-items: center;
    justify-content: center;
    text-align: center;
    padding: 0 36px;
  }
  .company-name {
    font-weight: 700;
    font-size: 32px;
    line-height: 1.2;
    margin-bottom: 22px;
  }
  .contact-icon {
    width: 26px;
    height: 26px;
    margin-bottom: 8px;
  }
  .address {
    font-weight: 400;
    font-size: 25px;
    line-height: 1.25;
    margin-bottom: 18px;
  }
  .phone {
    font-weight: 700;
    font-size: 27px;
  }
</style>
</head>
<body>
<main class="canvas">
  <section class="business-card">
    <div class="artwork-panel" role="img" aria-label="Pink plaid pattern background">
      <div class="dress-illustration" role="img" aria-label="Illustration of an elegant black and white lace dress on a dress form"></div>
    </div>
    <div class="info-panel">
      <div class="medallion">
        <div class="medallion-dots"></div>
        <div class="medallion-core">
          <h1 class="company-name">Valdet Apparel and<br>Accessories</h1>
          <svg class="contact-icon" viewBox="0 0 24 24" aria-hidden="true">
            <path fill="var(--icon-pink)" d="M12 2a7 7 0 0 0-7 7c0 5.2 7 13 7 13s7-7.8 7-13a7 7 0 0 0-7-7zm0 9.5A2.5 2.5 0 1 1 12 6.5a2.5 2.5 0 0 1 0 5z"/>
          </svg>
          <p class="address">3847 North Pelham St.<br>Los Angeles California</p>
          <svg class="contact-icon" viewBox="0 0 24 24" aria-hidden="true">
            <path fill="var(--icon-pink)" d="M4 9c0-2 3.6-4 8-4s8 2 8 4v2h-4V9.5c-1-.6-2.4-.9-4-.9s-3 .3-4 .9V11H4V9zm2 3h12l1 7H5l1-7zm6 1.5a2.5 2.5 0 1 0 0 5 2.5 2.5 0 0 0 0-5z"/>
          </svg>
          <p class="phone">424-639-8852</p>
        </div>
      </div>
    </div>
  </section>
</main>
</body>
</html>
```